Bref créative
Church stationary, door hangers, envelopes (large & small), and banner
Harvest Light Fellowship
We are a church concerned with our community, interested in reaching out to them with the love of God.
Religion and Spirituality
A.) Business card and stationery:
The envelope sizes are the standard #10 letter envelope and the standard large envelope size that a 8 1/2" x 11" piece of paper can fit into.
Please present designs with the current logo image that we have uploaded. Notice there are two styles, one with the church name in the logo and one image without it. Our current business card uses the logo image with the name of the church in it. We want to see designs using both logo images.
Name on business card: Dwight L. Barlow
Designation: Pastor
Business address: 2738 Kessler Mill Rd.
Phone numbers:
803-628-xxxx cell (we can add this number later)
803-472-1958 office
E-mail and website:
pastor@harvestlightfw.org
www.harvestlightfw.org
B.) Door hanger:
The door hanger size is approximately 4 1/2" wide x 12" tall.
Sample is attached. The back side should contain a map showing the directions to the church, service times, and a simple message inviting them to church
C.) Banner:
This should be a horizontal banner to be printed on a vinyl sign approximately 3' x 5'.
Include Tagline: Sunday 3:00 pm, Wednesday 7:30 pm
The image will be the church logo and name of the church. Also, included on the sign will be the times of the services, listed above. We are looking at using a white background for this sign.
Please see scanned image of our current business card layout. We want to see the business card presented with the name "Harvest Light" as part of the image and apart and to the right of the image. Thanks for your designs.
This is our current stationary.
We have uploaded a zip file with the logo vector files i.e. eps files. Hope this helps.
Thanks,
TM
Door hanger sample

```html
<!DOCTYPE html>
<html lang="en">
<head>
<meta charset="utf-8">
<title>Harvest Light Fellowship – Vinyl Banner</title>
<link href="https://fonts.googleapis.com/css2?family=Source+Sans+3:wght@400;600&display=swap" rel="stylesheet">
<style>
  :root {
    --teal: #0b7a80;
    --gold: #b8912a;
    --white: #ffffff;
    --caption: #111111;
    --stage-dark: #1c1c1c;
    --stage-mid: #7a7a7a;
    --stage-light: #ffffff;
    --stage-low: #c4c4c4;
  }
  html, body {
    margin: 0;
    padding: 0;
    overflow: hidden;
  }
  .canvas {
    position: relative;
    width: 1200px;
    height: 751px;
    overflow: hidden;
    background: linear-gradient(to bottom,
      var(--stage-dark) 0%,
      var(--stage-mid) 22%,
      var(--stage-light) 55%,
      var(--stage-light) 70%,
      var(--stage-low) 100%);
    font-family: "Source Sans 3", "Myriad Pro", sans-serif;
  }
  .banner {
    position: absolute;
    left: 101px;
    top: 43px;
    width: 998px;
    height: 605px;
    background: var(--teal);
  }
  .banner-field {
    position: absolute;
    left: 31px;
    top: 36px;
    width: 936px;
    height: 468px;
    overflow: hidden;
    background: var(--white);
  }
  .church-mark {
    position: absolute;
    left: 50%;
    top: 22px;
    transform: translateX(-50%);
    display: flex;
    align-items: center;
    gap: 18px;
  }
  .church-mark-square {
    width: 300px;
    height: 300px;
    background: var(--gold);
  }
  .church-mark-name {
    font-weight: 600;
    font-size: 36px;
    color: var(--gold);
    white-space: nowrap;
  }
  .church-name {
    position: absolute;
    left: 0;
    right: 0;
    top: 356px;
    margin: 0;
    text-align: center;
    font-weight: 600;
    font-size: 84px;
    line-height: 1;
    color: var(--gold);
    white-space: nowrap;
  }
  .service-times {
    position: absolute;
    left: 0;
    right: 0;
    top: 518px;
    margin: 0;
    text-align: center;
    font-weight: 400;
    font-size: 50px;
    line-height: 1;
    color: var(--white);
    white-space: nowrap;
  }
  .size-caption {
    position: absolute;
    left: 0;
    right: 0;
    top: 694px;
    margin: 0;
    text-align: center;
    font-family: Arial, "Helvetica Neue", sans-serif;
    font-size: 32px;
    line-height: 1;
    color: var(--caption);
  }
</style>
</head>
<body>
  <div class="canvas">
    <section class="banner">
      <div class="banner-field">
        <div class="church-mark">
          <div class="church-mark-square"></div>
          <span class="church-mark-name">HLF</span>
        </div>
        <h1 class="church-name">Harvest Light Fellowship</h1>
      </div>
      <p class="service-times">Sunday 3:00 pm | Wednesday 7:30 pm</p>
    </section>
    <p class="size-caption">5 ft W x 3 ft H</p>
  </div>
</body>
</html>
```